BHSC Business cards

We are an established dental practice that is looking for new business cards to match our new logo. We are looking for something unique and sophisticated.
BRIEF: Colours are black, silver and white. Include the company name, logo (including “Pelwick Heath Dental Care”) and phone number “03 9415 2876”.
Front - Include the company name, logo (including “Pelwick Heath Dental Care”) and phone number “03 9415 2876”.
Back - Include the company name,  “Pelwick Heath Dental Care”, phone number “03 9415 2876”. address "64A Tindle Street, Pelwick Heath, Vic 3187", "Email reception@pelwickheathdentalcare.com.au", the Dentist Name " Dr ................................"  Your next appointment "Day, date and time(am/pm)".  3 lines for 3 appointments please, and at the bottom "IF UNABLE TO KEEP THIS APPOINTMENT 48 HOURS NOTICE IS REQUIRED."
Try and be creative and different with the design, i've added an image for inspiration

Target Market(s)
ALL in need of dental
Industry/Entity Type
Dental Clinic
Look and feel
Each slider illustrates characteristics of the customer's brand and the style your logo design should communicate.

```html
<!DOCTYPE html>
<html lang="en">
<head>
<meta charset="utf-8">
<title>BHSC Business Cards</title>
<link rel="stylesheet" href="https://fonts.googleapis.com/css2?family=Montserrat:wght@600&family=Arimo:wght@400&display=swap">
<style>
  :root {
    --ink: #231f20;
    --silver: #d9dcd9;
    --paper: #ffffff;
    --stage: #e9e7e3;
    --rule: #3a3a3a;
  }
  * { box-sizing: border-box; margin: 0; padding: 0; }
  html, body { width: 1200px; height: 900px; overflow: hidden; }
  body {
    background: var(--stage);
    display: flex;
    flex-direction: column;
    align-items: center;
    justify-content: center;
    gap: 40px;
    font-family: "Arimo", Arial, sans-serif;
  }
  .card {
    width: 620px;
    height: 379px;
    position: relative;
    box-shadow: 0 6px 18px rgba(0,0,0,.18);
  }

  /* Front */
  .card-front {
    background: var(--ink);
    display: flex;
    align-items: center;
    justify-content: center;
    gap: 22px;
    color: var(--silver);
  }
  .brand-mark {
    width: 64px; height: 64px;
    border-radius: 50%;
    background: var(--silver);
    flex: none;
  }
  .brand-block { display: flex; flex-direction: column; gap: 8px; }
  .brand-name {
    font-family: "Montserrat", Arial, sans-serif;
    font-weight: 600;
    font-size: 25px;
    letter-spacing: 2px;
    line-height: 1.15;
  }
  .front-phone {
    font-family: "Montserrat", Arial, sans-serif;
    font-weight: 600;
    font-size: 15px;
    letter-spacing: 4px;
  }

  /* Back */
  .card-back {
    background: var(--paper);
    color: var(--ink);
    padding: 42px 40px 0 40px;
  }
  .back-head { display: flex; align-items: center; gap: 28px; }
  .back-mark {
    width: 92px; height: 92px;
    border-radius: 50%;
    border: 6px solid var(--ink);
    flex: none;
  }
  .contact-list { list-style: none; font-size: 15px; line-height: 1.45; }
  .dentist-line {
    margin-top: 18px;
    font-size: 17px;
    letter-spacing: .5px;
  }
  .appointments { margin-top: 14px; display: flex; flex-direction: column; gap: 12px; }
  .appt-row {
    display: flex;
    align-items: flex-end;
    font-size: 19px;
    gap: 6px;
  }
  .appt-row .blank { flex: 1; border-bottom: 1px solid var(--rule); height: 1px; margin-bottom: 5px; }
  .appt-row .ampm { font-size: 14px; }
  .notice-band {
    position: absolute;
    left: 0; right: 0; bottom: 0;
    height: 46px;
    background: var(--ink);
    color: var(--paper);
    display: flex;
    align-items: center;
    justify-content: center;
    font-size: 13px;
    letter-spacing: .5px;
  }
</style>
</head>
<body>
  <section class="card card-front" aria-label="Business card front">
    <span class="brand-mark"></span>
    <div class="brand-block">
      <p class="brand-name">PELWICK HEATH<br>DENTAL CARE</p>
      <p class="front-phone">03 9415 2876</p>
    </div>
  </section>

  <section class="card card-back" aria-label="Appointment card back">
    <div class="back-head">
      <span class="back-mark"></span>
      <ul class="contact-list">
        <li>03 9415 2876</li>
        <li>reception@pelwickheathdentalcare.com.au</li>
        <li>64A Tindle Street, Pelwick Heath, Vic 3187</li>
      </ul>
    </div>
    <p class="dentist-line">THE DENTIST NAME " DR ...................................."</p>
    <div class="appointments">
      <div class="appt-row"><span>DATE</span><span class="blank"></span><span>AT</span><span class="blank"></span><span class="ampm">AM/PM</span></div>
      <div class="appt-row"><span>DATE</span><span class="blank"></span><span>AT</span><span class="blank"></span><span class="ampm">AM/PM</span></div>
      <div class="appt-row"><span>DATE</span><span class="blank"></span><span>AT</span><span class="blank"></span><span class="ampm">AM/PM</span></div>
    </div>
    <p class="notice-band">IF UNABLE TO KEEP THIS APPOINTMENT 48 HOURS NOTICE IS REQUIRED</p>
  </section>
</body>
</html>
```